Driver License Monitoring Application Marketing Website

We need a new web design for our web application. The product is called "PermitSentry." We provide a driver license monitoring service to companies and local government bodies with driver fleets. Our current website is available at www.PermitSentry-demo.net.

I prefer a clean, single-page design with good SEO. Attached are some PDFs with data about the project.

Target Market(s)

Companies with driver fleets, local government.

Industry/Entity Type

Government

Coding

Coded - Design and coding required

Number of Pages Required

1 page

Colors
000000

Requirements
Must have
• Content from current www.PermitSentry-demo.net and attached PDFs.
Nice to have
• Prefer a simple Bootstrap or similar design for easy editing.
• Room for a simple video explanation of how the product works (we don't have an actual video yet)

```html
<!DOCTYPE html>
<html lang="en">
<head>
<meta charset="utf-8">
<title>PermitSentry – Florida Driver License Monitoring</title>
<link rel="stylesheet" href="https://fonts.googleapis.com/css2?family=Cinzel:wght@400;700&family=Open+Sans:wght@400;600&family=Cabin:wght@400;600&display=swap">
<style>
:root{
  --red:#d0262f;
  --red-deep:#a8222a;
  --black:#0b0b0b;
  --ink:#333333;
  --grey:#777777;
  --light:#f3f3f7;
  --white:#ffffff;
  --dark-band:#1b1b1d;
}
*{box-sizing:border-box;margin:0;padding:0}
html,body{width:1200px;height:2487px;overflow:hidden}
body{position:relative;background:var(--white);font-family:"Open Sans",Arial,sans-serif;color:var(--ink)}
.abs{position:absolute}

/* top bar */
.topbar{left:0;top:0;width:1200px;height:25px;background:var(--black);display:flex;justify-content:flex-end;align-items:center;padding-right:150px;gap:10px;font-size:12px;color:var(--white)}
.topbar .label{color:var(--red)}
.topbar .social{display:flex;gap:6px;margin-left:12px}
.topbar .social span{width:8px;height:8px;border-radius:50%;background:#bbb;display:block}

/* header */
.header{left:0;top:25px;width:1200px;height:103px;background:var(--white)}
.logo{position:absolute;left:172px;top:38px;font-family:"Cinzel",serif;font-weight:700;font-size:27px;color:var(--black);letter-spacing:.5px;display:flex;align-items:center;gap:9px}
.logo .mark{width:14px;height:14px;background:var(--red);display:block}
.nav{position:absolute;left:514px;top:37px;display:flex;gap:6px;font-family:"Cabin",sans-serif;font-size:15px;color:#888}
.nav a{display:block;padding:7px 16px;color:inherit;text-decoration:none}
.nav a.active{border:1px solid var(--red);color:var(--red)}

/* hero */
.hero{left:0;top:128px;width:1200px;height:535px;background:radial-gradient(ellipse at 30% 70%,#7a3a12 0%,#3a1c0d 35%,#140d08 70%,#090705 100%)}
.hero-photo{position:absolute;inset:0}
.hero-overlay{position:absolute;left:240px;top:157px;width:730px;height:288px;background:rgba(0,0,0,.25)}
.hero h1{position:absolute;left:0;width:1200px;top:168px;text-align:center;font-family:"Cinzel",serif;font-weight:700;font-size:37px;color:var(--white);letter-spacing:.5px}
.hero p{position:absolute;left:255px;width:690px;top:226px;text-align:center;font-family:"Cinzel",serif;font-size:19px;line-height:26px;color:var(--white)}
.hero p b{font-weight:700}
.hero .btn{position:absolute;left:493px;top:473px;width:212px;height:49px;background:var(--red-deep);color:var(--white);font-family:"Cinzel",serif;padding:7px 0 0 28px}
.hero .btn strong{display:block;font-size:16px;line-height:18px}
.hero .btn small{display:block;font-size:12px;color:#f2c8c8}
.hero .btn svg{position:absolute;right:18px;top:16px}
.arrow{position:absolute;top:330px}
.dots{position:absolute;top:647px;left:570px;display:flex;gap:5px}
.dots span{width:8px;height:8px;border-radius:50%;border:1px solid #fff;display:block}
.dots span.on{background:var(--red);border-color:var(--red)}

/* what we do */
.icons{left:463px;top:677px;display:flex;gap:34px}
.icons .circle{width:68px;height:68px;border-radius:50%;border:2px solid var(--red);display:flex;align-items:center;justify-content:center}
.section-title{left:0;width:1200px;text-align:center;font-family:"Cinzel",serif;font-weight:700;color:var(--red)}
.what-title{top:768px;font-size:26px}
.what-sub{left:0;width:1200px;top:801px;text-align:center;font-family:"Cinzel",serif;font-size:11px;color:var(--grey)}
.what-text{left:205px;width:790px;top:836px;text-align:center;font-size:13.5px;line-height:21px;color:#555}

/* sector bands */
.sector{left:0;width:728px;height:270px;padding:28px 0 0 200px;color:var(--white)}
.sector.commercial{top:962px;background:linear-gradient(90deg,#b72a30 0%,#c0383c 60%,#8e2327 100%)}
.sector.government{top:1232px;background:linear-gradient(90deg,#141416 0%,#2a2a2c 70%,#1a1a1c 100%)}
.sector h2{font-family:"Cinzel",serif;font-weight:700;font-size:27px;line-height:34px}
.sector h2 span{font-size:21px}
.sector h3{font-family:"Cinzel",serif;font-weight:700;font-size:20px;margin-top:8px}
.sector p{font-size:13px;line-height:21px;margin-top:12px;width:490px;color:#f0e0e0}
.sector.government p{color:#ccc}
.sector .more{display:flex;align-items:center;gap:9px;margin-top:18px;font-family:"Cinzel",serif;font-size:11px}
.media{left:728px;width:472px;height:270px;display:flex;align-items:center;justify-content:center}
.media.control{top:962px;background:linear-gradient(135deg,#4a3a2a 0%,#7c6a52 40%,#2e2822 100%)}
.media.keyboard{top:1232px;background:linear-gradient(135deg,#c9d6ea 0%,#8fa6c8 55%,#5e779e 100%)}

/* call to action */
.cta{left:0;top:1502px;width:1200px;height:156px}
.cta-text{left:0;width:1200px;top:1547px;text-align:center;font-family:"Cinzel",serif;font-weight:700;font-size:18px;line-height:26px;color:var(--white)}
.cta-phone{left:0;width:1200px;top:1600px;text-align:center;font-family:"Cabin",sans-serif;font-size:28px;color:var(--red)}

/* monitor */
.laptop{left:176px;top:1734px}
.monitor-title{left:551px;top:1728px;width:460px;font-family:"Cinzel",serif;font-size:28px;line-height:36px;color:var(--red)}
.features{left:540px;top:1846px;display:flex}
.feature{width:196px;text-align:center;font-family:"Cinzel",serif;font-size:14px;color:#666}
.feature .ic{width:34px;height:34px;margin:0 auto 10px;border:2px solid var(--red);border-radius:50%;display:flex;align-items:center;justify-content:center}

/* trusted */
.trusted{left:0;top:2007px;width:1200px;height:325px;background:var(--light)}
.notch{left:578px;top:2007px}
.trusted-title{left:0;width:1200px;top:2032px;text-align:center;font-family:"Cinzel",serif;font-size:20px;color:#444}
.trusted-rule{left:470px;top:2068px;width:260px;height:1px;background:#ccc}
.partners{left:176px;top:2083px;width:860px;display:grid;grid-template-columns:190px 222px 250px 198px}
.partner{height:94px;display:flex;align-items:center;justify-content:center;gap:8px;font-family:"Cinzel",serif;font-size:20px;color:#9a9a9a;border-right:1px solid #e0e0e4;border-bottom:1px solid #e0e0e4}
.partner:nth-child(4n){border-right:none}
.partner:nth-child(n+5){border-bottom:none}
.partner .dot{width:12px;height:12px;border-radius:50%;background:#b5b5b5}

/* footer */
.footer{left:0;top:2332px;width:1200px;height:155px;background:linear-gradient(180deg,#3a3a3a 0%,#2b2b2b 100%)}
.footer-links{left:0;width:1200px;top:2358px;display:flex;justify-content:center;gap:14px;font-family:"Cabin",sans-serif;font-size:14px;color:var(--white)}
.footer-links .sep{width:5px;height:5px;border-radius:50%;background:var(--red);align-self:center}
.footer-social{left:0;width:1200px;top:2389px;display:flex;justify-content:center;gap:7px}
.footer-social span{width:9px;height:9px;border-radius:50%;background:var(--red);display:block}
.footer-line{left:0;width:1200px;text-align:center;font-size:14px;color:var(--white);display:flex;justify-content:center;align-items:center;gap:8px}
.footer-email{top:2417px}
.footer-phone{top:2448px}
.copyright{right:150px;top:2466px;font-size:10px;color:#ccc}
</style>
</head>
<body>

<div class="abs topbar">
  <span class="label">Call Us</span><span>555-010-4821</span>
  <div class="social"><span></span><span></span><span></span><span></span></div>
</div>

<header class="abs header">
  <div class="logo"><span class="mark"></span>PermitSentry</div>
  <nav class="nav">
    <a class="active">Home</a><a>License Monitoring</a><a>About Us</a><a>Contact</a><a>Client Login</a>
  </nav>
</header>

<section class="abs hero">
  <div class="hero-photo" role="img" aria-label="Fuel tanker truck driving on a highway at dusk with city lights"></div>
  <div class="hero-overlay"></div>
  <h1>FLORIDA DRIVER LICENSE MONITORING</h1>
  <p>Monitor your fleet <b>electronically.</b> Get alerts by <b>email</b> and <b>online</b>. Never let another unlicensed or unauthorized driver behind the <b>wheel.</b></p>
  <div class="btn"><strong>MORE INFO</strong><small>Track your fleet</small>
    <svg width="10" height="16" viewBox="0 0 10 16"><path d="M2 2l6 6-6 6" stroke="#fff" stroke-width="2" fill="none"/></svg>
  </div>
  <svg class="arrow" style="left:8px" width="18" height="40" viewBox="0 0 18 40"><path d="M15 2L3 20l12 18" stroke="#fff" stroke-width="2" fill="none"/></svg>
  <svg class="arrow" style="right:8px" width="18" height="40" viewBox="0 0 18 40"><path d="M3 2l12 18L3 38" stroke="#fff" stroke-width="2" fill="none"/></svg>
  <div class="dots"><span class="on"></span><span></span><span></span></div>
</section>

<div class="abs icons">
  <div class="circle"><svg width="34" height="26" viewBox="0 0 34 26"><rect x="1" y="3" width="32" height="22" rx="2" fill="#d0262f"/><rect x="12" y="0" width="10" height="5" fill="#d0262f"/><circle cx="10" cy="12" r="4" fill="#fff"/><rect x="4" y="17" width="12" height="4" fill="#fff"/><rect x="19" y="10" width="10" height="2" fill="#fff"/><rect x="19" y="15" width="10" height="2" fill="#fff"/></svg></div>
  <div class="circle"><svg width="28" height="34" viewBox="0 0 28 34"><rect x="2" y="4" width="22" height="28" rx="2" fill="#d0262f"/><rect x="8" y="1" width="10" height="6" fill="#d0262f" stroke="#fff"/><path d="M7 14h12M7 19h12M7 24h8" stroke="#fff" stroke-width="2"/><path d="M26 8l-8 14" stroke="#d0262f" stroke-width="3"/></svg></div>
  <div class="circle"><svg width="40" height="28" viewBox="0 0 40 28"><rect x="1" y="8" width="22" height="12" fill="#d0262f"/><path d="M23 10h8l6 6v4H23z" fill="#d0262f"/><rect x="10" y="2" width="4" height="8" fill="#d0262f"/><circle cx="8" cy="22" r="4" fill="#d0262f" stroke="#fff" stroke-width="1.5"/><circle cx="30" cy="22" r="4" fill="#d0262f" stroke="#fff" stroke-width="1.5"/></svg></div>
</div>

<h2 class="abs section-title what-title">WHAT WE DO</h2>
<div class="abs what-sub">License Monitoring</div>
<p class="abs what-text">How many of your drivers currently have a suspended license? The answer may surprise you. Driving with a suspended license is the most commonly committed offense in America. In 2011, over 1.8 million licenses got suspended in Florida. With just over 15 million drivers, that's 12% of all licensed Florida drivers.</p>

<section class="abs sector commercial" role="region" aria-label="Commercial private sector">
  <h2>COMMERCIAL <span>Private Sector</span></h2>
  <h3>Monitor your fleet's driver licenses</h3>
  <p>The private sector is fraught with risk. Having an unlicensed or unqualified driver poses an extreme hazard for companies on the road....</p>
  <div class="more"><svg width="14" height="10" viewBox="0 0 14 10"><ellipse cx="7" cy="5" rx="6.5" ry="4.5" fill="#fff"/><circle cx="7" cy="5" r="2" fill="#b72a30"/></svg>READ MORE</div>
</section>
<div class="abs media control" role="img" aria-label="Operator watching a wall of monitoring screens">
  <svg width="52" height="52" viewBox="0 0 52 52"><circle cx="26" cy="26" r="24" fill="rgba(0,0,0,.25)" stroke="#fff" stroke-width="2"/><path d="M21 16l14 10-14 10z" fill="#fff"/></svg>
</div>

<section class="abs sector government" role="region" aria-label="Government public sector">
  <h2>GOVERNMENT <span>Public Sector</span></h2>
  <h3>Electronic oversight for government clients</h3>
  <p>Public safety is the primary responsibility of all government organizations, regardless of the size of your fleet. Using PermitSentry, you can be confident that your drivers are properly licensed and authorized to operate a motor vehicle....</p>
  <div class="more"><svg width="14" height="10" viewBox="0 0 14 10"><ellipse cx="7" cy="5" rx="6.5" ry="4.5" fill="#fff"/><circle cx="7" cy="5" r="2" fill="#222"/></svg>READ MORE</div>
</section>
<div class="abs media keyboard" role="img" aria-label="Close-up of a keyboard with a government key">
  <svg width="52" height="52" viewBox="0 0 52 52"><circle cx="26" cy="26" r="24" fill="rgba(0,0,0,.2)" stroke="#fff" stroke-width="2"/><path d="M21 16l14 10-14 10z" fill="#fff"/></svg>
</div>

<svg class="abs cta" width="1200" height="156" viewBox="0 0 1200 156"><path d="M0 0H1200V142L600 156L0 142Z" fill="#0e0e0e"/></svg>
<p class="abs cta-text">Don't Spend Another Day in the Dark About Your Drivers Call Now<br>to Start Monitoring.</p>
<div class="abs cta-phone">(555-010-4821)</div>

<svg class="abs laptop" width="364" height="190" viewBox="0 0 364 190" role="img" aria-label="Laptop showing the monitoring dashboard summary">
  <rect x="40" y="2" width="284" height="168" rx="6" fill="#1e1e1e"/>
  <rect x="48" y="10" width="268" height="152" fill="#f6f6f6"/>
  <rect x="48" y="10" width="268" height="10" fill="#e4e4e4"/>
  <rect x="52" y="24" width="40" height="134" fill="#e9e9ee"/>
  <rect x="98" y="26" width="60" height="8" fill="#555"/>
  <rect x="98" y="40" width="160" height="110" fill="#fff" stroke="#ddd"/>
  <g fill="#d0262f"><rect x="104" y="48" width="40" height="6"/><rect x="104" y="62" width="40" height="6"/><rect x="104" y="76" width="40" height="6"/><rect x="104" y="90" width="40" height="6"/></g>
  <rect x="264" y="40" width="46" height="20" fill="#cfe0f2"/>
  <path d="M0 172H364L352 186H12Z" fill="#cfcfcf"/>
</svg>
<h2 class="abs monitor-title">Monitor your Whole Fleet Online</h2>
<div class="abs features">
  <div class="feature"><div class="ic"><svg width="16" height="18" viewBox="0 0 16 18"><rect x="2" y="8" width="12" height="9" fill="#d0262f"/><path d="M5 8V5a3 3 0 016 0v3" stroke="#d0262f" stroke-width="2" fill="none"/></svg></div>Secure</div>
  <div class="feature"><div class="ic"><svg width="18" height="18" viewBox="0 0 18 18"><circle cx="9" cy="9" r="7" stroke="#d0262f" stroke-width="2" fill="none"/><path d="M9 5v4l3 2" stroke="#d0262f" stroke-width="2" fill="none"/></svg></div>Available 24hours a day</div>
  <div class="feature"><div class="ic"><svg width="18" height="16" viewBox="0 0 18 16"><rect x="1" y="1" width="12" height="9" stroke="#d0262f" stroke-width="2" fill="none"/><rect x="11" y="6" width="6" height="9" fill="#d0262f"/></svg></div>Desktop or Mobile</div>
</div>

<section class="abs trusted" aria-label="Trusted by the best"></section>
<svg class="abs notch" width="44" height="14" viewBox="0 0 44 14"><path d="M0 0H44L22 14Z" fill="#fff"/></svg>
<h2 class="abs trusted-title">TRUSTED BY THE BEST</h2>
<div class="abs trusted-rule"></div>
<div class="abs partners">
  <div class="partner"><span class="dot"></span>Norvane</div>
  <div class="partner"><span class="dot"></span>Petrix</div>
  <div class="partner"><span class="dot"></span>Halvor</div>
  <div class="partner"><span class="dot"></span>Kestrel Motors</div>
  <div class="partner"><span class="dot"></span>Corbel</div>
  <div class="partner"><span class="dot"></span>Tavola Grill</div>
  <div class="partner"><span class="dot"></span>Brennick</div>
  <div class="partner"><span class="dot"></span>Ashford &amp; Lyle</div>
</div>

<footer class="abs footer" role="img" aria-label="Faint street map background"></footer>
<div class="abs footer-links"><span>Home</span><span class="sep"></span><span>About Us</span><span class="sep"></span><span>Contact</span></div>
<div class="abs footer-social"><span></span><span></span><span></span><span></span></div>
<div class="abs footer-line footer-email"><svg width="18" height="12" viewBox="0 0 18 12"><rect x="1" y="1" width="16" height="10" stroke="#fff" fill="none"/><path d="M1 1l8 6 8-6" stroke="#fff" fill="none"/></svg>contact@permitsentry-demo.net</div>
<div class="abs footer-line footer-phone"><svg width="10" height="16" viewBox="0 0 10 16"><rect x="1" y="1" width="8" height="14" rx="1.5" fill="#fff"/><rect x="2.5" y="3" width="5" height="8" fill="#333"/></svg>1.555.010.4821</div>
<div class="abs copyright">Copyright © 2015 PermitSentry-demo.net</div>

</body>
</html>
```